bramblegate crest roofing flyer*

I need an a5 size flyer designing to go in our local advertising magazine.We are based in the north west of England Id like key features from the website including on the flyer, possibly even reviews, what we do ect.I don't however want it too busy, simple pictures and description of service.company colours and logo. I require simple one sided business cards toonumber, web address and logowinner will receive a request to design around 5 different double sided a5 flyers too, each with all our services on one side and the other primarily for one service we have provided locally with a spacve to put the house number down.REPAIRSROOFLINEFLAT ROOFS PITCHED ROOFSSYNTHETIC ROOFSUP TO 50 YEARS WARRANTY AVAILABLERANKED THE #1 FLAT ROOFER IN THE UK OUT OF 787 REGISTERED FLAT ROOFING COMPANIESRANKED THE #10 ROOFING COMPANY IN THE UK OUT OF 1976 REGISTERED SPECIALIST ROOFING COMPANIESBOTH FOR COST, CUSTOMER SERVICE AND QUALITY WITH 5 STAR REVIEWSGUARANTEED TO FIND AND FIX A LEAKAPPROVED INSTALLERSAWARD WINNINGTIME SERVED FIXED PRICES

Target Market(s)

homeowners

Colors

Designer to choose only greyscale colors for use in the design.

Requirements
Must have
• contact details
• pictures of my work
• clear and simple

```html
<!DOCTYPE html>
<html lang="en">
<head>
<meta charset="utf-8">
<title>Bramblegate Crest Roofing – Flyer</title>
<link href="https://fonts.googleapis.com/css2?family=Oswald:wght@500;600;700&family=Open+Sans:ital,wght@0,400;0,600;0,700;1,400&display=swap" rel="stylesheet">
<style>
  :root{
    --green:#3c9a3b;
    --green-light:#6cbb4f;
    --green-dark:#2e7d2e;
    --charcoal:#323234;
    --ink:#3a3a3a;
    --yellow:#f3c41d;
    --white:#ffffff;
    --page:#eeeeee;
    --photo-roof:#5d6570;
    --photo-sky:#b9c7d6;
    --photo-brick:#8a5a48;
    --photo-slate:#7b7f83;
  }
  html,body{margin:0;padding:0;width:999px;height:1200px;overflow:hidden;background:var(--page);}
  .flyer{
    position:absolute;left:100px;top:33px;width:420px;height:595px;
    background:var(--white);overflow:hidden;
    transform:scale(1.9048);transform-origin:top left;
    box-shadow:0 0 3px rgba(0,0,0,.15);
    font-family:"Open Sans",Arial,sans-serif;color:var(--ink);
  }
  .header-art{position:absolute;left:0;top:0;width:420px;height:290px;}
  .brand{
    position:absolute;left:12px;top:26px;margin:0;
    font-family:"Oswald",Arial,sans-serif;font-weight:700;font-size:27px;line-height:28px;
    color:var(--white);letter-spacing:.5px;text-transform:uppercase;
  }
  .warranty{
    position:absolute;left:12px;top:122px;margin:0;
    font-family:"Oswald",Arial,sans-serif;font-weight:500;font-size:16px;line-height:21px;
    color:var(--white);
  }
  .promise{
    position:absolute;right:10px;top:229px;margin:0;text-align:right;
    font-family:"Oswald",Arial,sans-serif;font-weight:600;font-size:12.5px;line-height:17px;
    color:var(--yellow);
  }
  .services-title{
    position:absolute;left:19px;top:219px;margin:0;
    font-family:"Oswald",Arial,sans-serif;font-weight:700;font-size:17px;letter-spacing:1px;
    color:var(--green);
  }
  .services{position:absolute;left:20px;top:254px;margin:0;padding:0;list-style:none;}
  .services li{
    display:flex;align-items:center;height:35px;
    font-family:"Oswald",Arial,sans-serif;font-weight:500;font-size:14px;color:var(--ink);
  }
  .services svg{width:24px;height:24px;margin-right:13px;}
  .rankings{position:absolute;left:210px;top:291px;display:flex;gap:4px;}
  .rank{position:relative;width:64px;height:84px;}
  .rank svg{position:absolute;left:0;top:0;}
  .rank-text{
    position:relative;padding:9px 5px 0;text-align:center;
    font-size:4.6px;line-height:6px;font-weight:700;color:var(--white);text-transform:uppercase;
  }
  .rank-num{display:block;font-family:"Oswald",Arial,sans-serif;font-size:12px;line-height:13px;color:var(--yellow);}
  .stars{display:block;color:var(--yellow);font-size:8px;letter-spacing:-.5px;line-height:11px;}
  .gallery{position:absolute;left:12px;top:395px;display:flex;gap:6px;}
  .work-photo{width:129px;height:86px;}
  .review{position:absolute;left:22px;top:486px;width:376px;text-align:center;}
  .review-stars{color:var(--yellow);font-size:10px;letter-spacing:1px;}
  .review p{margin:3px 0 0;font-style:italic;font-size:7.6px;line-height:10.5px;color:var(--ink);}
  .call-bar{
    position:absolute;left:0;top:546px;width:420px;height:25px;background:var(--green);
    display:flex;align-items:center;justify-content:center;gap:26px;
    font-family:"Oswald",Arial,sans-serif;font-weight:500;font-size:13px;color:var(--white);
  }
  .phone{display:flex;align-items:center;gap:5px;}
  .website{
    position:absolute;left:0;top:577px;width:420px;text-align:center;margin:0;
    font-weight:700;font-size:9.5px;letter-spacing:.4px;color:var(--ink);
  }
</style>
</head>
<body>
<main class="flyer">
  <svg class="header-art" viewBox="0 0 420 290" aria-hidden="false">
    <defs>
      <linearGradient id="roofTone" x1="0" y1="0" x2="0" y2="1">
        <stop offset="0" stop-color="#4a5560"/><stop offset=".55" stop-color="#6c737b"/><stop offset="1" stop-color="#9aa0a4"/>
      </linearGradient>
    </defs>
    <rect class="header-green" x="0" y="0" width="420" height="208" fill="var(--green)"/>
    <polygon class="accent-stripe" points="262,0 300,0 172,208 134,208" fill="var(--green-light)"/>
    <polygon class="accent-stripe" points="210,0 228,0 100,208 82,208" fill="var(--green-dark)" opacity=".5"/>
    <polygon class="hero-photo" role="img" aria-label="Photo of a finished dormer roof in dark grey shingles on a white-trimmed house" points="314,0 420,0 420,208 186,208" fill="url(#roofTone)"/>
    <polygon class="promise-band" points="178,208 420,208 420,283 236,283" fill="var(--charcoal)"/>
    <circle class="award-seal" cx="377" cy="201" r="21" fill="var(--yellow)" stroke="var(--white)" stroke-width="2"/>
  </svg>

  <h1 class="brand">Bramblegate<br>Crest Roofing</h1>
  <p class="warranty">UP TO 50 YEARS<br>WARRANTY AVAILABLE</p>
  <p class="promise">AWARD WINNING TIME SERVED<br>FIXED PRICES</p>

  <h2 class="services-title">SPECIALSING IN</h2>
  <ul class="services">
    <li><svg viewBox="0 0 24 24"><circle cx="12" cy="12" r="12" fill="var(--green)"/><path d="M5 13l7-6 7 6v5H5z" fill="var(--yellow)"/></svg>REPAIRS ROOF</li>
    <li><svg viewBox="0 0 24 24"><circle cx="12" cy="12" r="12" fill="var(--green)"/><rect x="5" y="9" width="14" height="7" fill="var(--yellow)"/></svg>LINE FLAT ROOFS</li>
    <li><svg viewBox="0 0 24 24"><circle cx="12" cy="12" r="12" fill="var(--green)"/><path d="M6 17V8h9v3H9v6z" fill="var(--yellow)"/></svg>PITCHED ROOFS</li>
    <li><svg viewBox="0 0 24 24"><circle cx="12" cy="12" r="12" fill="var(--green)"/><path d="M4 15l8-8 8 8h-3l-5-5-5 5z" fill="var(--yellow)"/></svg>SYNTHETIC ROOF</li>
  </ul>

  <div class="rankings">
    <div class="rank">
      <svg width="64" height="84" viewBox="0 0 64 84"><path d="M0 0H64V68L32 84L0 68Z" fill="var(--green)" stroke="var(--white)" stroke-width="1.5"/></svg>
      <div class="rank-text"><span class="rank-num">#1</span>Ranked the #1 flat roofer in the UK out of 787 registered flat roofing companies</div>
    </div>
    <div class="rank">
      <svg width="64" height="84" viewBox="0 0 64 84"><path d="M0 0H64V68L32 84L0 68Z" fill="var(--green)" stroke="var(--white)" stroke-width="1.5"/></svg>
      <div class="rank-text"><span class="rank-num">#10</span>Ranked the #10 roofing company in the UK out of 1976 registered specialist roofing companies</div>
    </div>
    <div class="rank">
      <svg width="64" height="84" viewBox="0 0 64 84"><path d="M0 0H64V68L32 84L0 68Z" fill="var(--green)" stroke="var(--white)" stroke-width="1.5"/></svg>
      <div class="rank-text"><span class="stars">★★★★★</span>Customer service and quality with 5 star reviews guaranteed to find &amp; fix a leak approved installers</div>
    </div>
  </div>

  <div class="gallery">
    <svg class="work-photo" role="img" aria-label="Work photo: new rubber flat roof on a brick extension" viewBox="0 0 129 86"><defs><linearGradient id="g1" x1="0" y1="0" x2="0" y2="1"><stop offset="0" stop-color="var(--photo-sky)"/><stop offset=".45" stop-color="#8c7a6c"/><stop offset="1" stop-color="var(--photo-brick)"/></linearGradient></defs><rect width="129" height="86" fill="url(#g1)"/></svg>
    <svg class="work-photo" role="img" aria-label="Work photo: brick chimney with new lead flashing on a slate roof" viewBox="0 0 129 86"><defs><linearGradient id="g2" x1="0" y1="0" x2="0" y2="1"><stop offset="0" stop-color="var(--photo-sky)"/><stop offset=".4" stop-color="var(--photo-brick)"/><stop offset="1" stop-color="var(--photo-slate)"/></linearGradient></defs><rect width="129" height="86" fill="url(#g2)"/></svg>
    <svg class="work-photo" role="img" aria-label="Work photo: red brick house with renewed pitched roof" viewBox="0 0 129 86"><defs><linearGradient id="g3" x1="0" y1="0" x2="0" y2="1"><stop offset="0" stop-color="#a9c0da"/><stop offset=".35" stop-color="var(--photo-roof)"/><stop offset="1" stop-color="var(--photo-brick)"/></linearGradient></defs><rect width="129" height="86" fill="url(#g3)"/></svg>
  </div>

  <div class="review">
    <div class="review-stars">★★★★★</div>
    <p>Excellent job done of re roofing my extension roof in rubber tiles looks great the lads were very polite and professional in all aspects of the job would definitely recommend them to anyone thanks again dan.</p>
  </div>

  <div class="call-bar">
    <span>CALL TODAY FOR YOUR FREE QUOTE</span>
    <span class="phone"><svg width="12" height="12" viewBox="0 0 24 24"><path d="M6.6 10.8a15 15 0 0 0 6.6 6.6l2.2-2.2a1 1 0 0 1 1-.25 11.4 11.4 0 0 0 3.6.57 1 1 0 0 1 1 1V20a1 1 0 0 1-1 1A17 17 0 0 1 3 4a1 1 0 0 1 1-1h3.5a1 1 0 0 1 1 1c0 1.25.2 2.45.57 3.57a1 1 0 0 1-.25 1z" fill="var(--white)"/></svg>07700 900123</span>
  </div>
  <p class="website">www.bramblegatecrestroofing.com</p>
</main>
</body>
</html>
```